Website for virtual assistant and proofreader

Professional, feminine (but not flowery!) website offering and explaining my services as a VA and Proofreader. Probably only 7 pages: home, about, services (x2), fees, testimonials and contact page. <br/><br/>I already have most of the content, which I have uploaded so you can get an idea of waht I do. I have brand colours and logo already also uploaded. I really just need the bones of the site to be designed and am happy/capable of setting this up as a Wordpress site. I'm just rubbish at design!

Industry/Entity Type

Business Service

Coding

Coded - Design and coding required

Number of Pages Required

4 page

Other font styles liked:
• Roboto Bold + Great Vibes

Colors
3276b5
fee3d4

Requirements
Must have
• should be informative, professional, feminine. Clean, clear, CTA's links to services and fees pages
• Also, see all 3 colour codes on the attached doc.
Nice to have
• business images but place holders will do
Should not have
• Nothing flowery or cartoons! Not 'busy'

```html
<!DOCTYPE html>
<html lang="en">
<head>
<meta charset="utf-8">
<title>Maren K Holt – Virtual Assistant and Proofreader</title>
<link href="https://fonts.googleapis.com/css2?family=Great+Vibes&family=Roboto:wght@400;500;700&display=swap" rel="stylesheet">
<style>
:root{
  --blue:#1b6496;
  --blue-bright:#3276b5;
  --blush:#fee3d4;
  --taupe:#8b8180;
  --ink:#3d3d3d;
  --muted:#666;
  --dark:#232323;
  --white:#fff;
  --star:#f5a623;
}
*{box-sizing:border-box;margin:0;padding:0}
html,body{width:1200px;height:3019px;overflow:hidden}
body{font-family:'Roboto',sans-serif;color:var(--ink);background:var(--white);position:relative}
.script{font-family:'Great Vibes',cursive;font-weight:400}
section,header,footer{position:absolute;left:0;width:1200px;overflow:hidden}
.abs{position:absolute}
.btn{display:inline-block;background:var(--blue);color:var(--white);font-weight:700;font-size:10px;letter-spacing:.3px;text-transform:uppercase;width:125px;height:32px;line-height:32px;text-align:center;border-radius:2px;text-decoration:none}

/* header */
.site-header{top:0;height:90px;border-top:3px solid var(--blue);background:var(--white);z-index:2;overflow:visible}
.brand{position:absolute;left:216px;top:-3px;width:186px;height:108px;background:var(--white);border-radius:0 0 93px 93px;display:flex;align-items:center;justify-content:center;gap:8px}
.brand-dot{width:26px;height:26px;border-radius:50%;background:var(--blue)}
.brand-name{font-size:15px;font-weight:500;color:var(--blue)}
.contact-bar{position:absolute;right:236px;top:22px;display:flex;gap:28px;font-size:11.5px;color:var(--muted)}
.contact-bar span{display:flex;align-items:center;gap:8px}
.nav{position:absolute;right:236px;top:58px;display:flex;gap:23px;font-size:9px;font-weight:700;color:var(--ink)}
.nav .active{color:var(--blue)}

/* hero */
.hero{top:90px;height:365px;background:linear-gradient(120deg,#b9b6b2 0%,#e4e1dc 35%,#cfc8c0 60%,#a88d73 100%)}
.hero-shade{position:absolute;inset:0;background:linear-gradient(90deg,rgba(40,40,40,.35),rgba(40,40,40,.05))}
.hero h1{position:absolute;left:234px;top:110px;font-size:62px;color:var(--white);line-height:1}
.hero p{position:absolute;left:234px;top:188px;font-size:19px;font-weight:700;color:var(--white)}
.hero .btn{position:absolute;left:234px;top:233px}

/* welcome */
.welcome{top:455px;height:551px}
.welcome-band{position:absolute;left:778px;top:0;width:422px;height:551px;background:var(--blue)}
.welcome h2{position:absolute;left:234px;top:50px;font-size:44px;color:var(--blue)}
.welcome-text{position:absolute;left:234px;top:116px;width:378px;font-size:9.6px;line-height:12px}
.welcome-text p{margin-bottom:12px}
.welcome .btn{position:absolute;left:234px;top:453px}
.portrait{position:absolute;left:645px;top:61px;width:372px;height:425px;background:linear-gradient(160deg,#b07a4e,#6e3f24 55%,#d9b29a)}

/* services */
.services{top:1006px;height:409px;background:var(--taupe)}
.services h2{position:absolute;top:30px;width:100%;text-align:center;font-size:44px;color:var(--white)}
.services-intro{position:absolute;left:278px;top:92px;width:644px;text-align:center;font-size:9.6px;line-height:16px;color:var(--white);font-weight:500}
.cards{position:absolute;left:234px;top:165px;display:flex;gap:19px}
.card{width:169px;height:198px;background:var(--white);border-radius:2px;text-align:center;padding-top:19px}
.card-icon{width:55px;height:55px;border-radius:50%;background:var(--blue);margin:0 auto 14px}
.card h3{font-size:11.5px;font-weight:500;line-height:19px;color:#222;margin-bottom:6px}
.card p{font-size:9.4px;line-height:16px;color:var(--muted);padding:0 8px}
.card a{font-size:8.5px;font-weight:700;color:var(--blue);text-decoration:underline}

/* about */
.about{top:1415px;height:702px}
.tagline{position:absolute;top:45px;width:100%;text-align:center;font-size:38px;color:var(--blue)}
.col{position:absolute;top:120px;font-size:9.4px;line-height:12px}
.col-left{left:234px;width:354px}
.col-right{left:611px;width:360px}
.col h3{font-size:27px;color:var(--blue);line-height:30px;margin-bottom:14px}
.col p{margin-bottom:12px}
.col h3.gap{margin-top:26px}

/* certifications */
.certs{top:2117px;height:227px;background:var(--blue)}
.certs h2{position:absolute;top:38px;width:100%;text-align:center;font-size:15px;font-weight:700;color:var(--white)}
.cert-list{position:absolute;top:82px;list-style:none;font-size:9.8px;font-weight:500;color:var(--white)}
.cert-list li{height:22.5px;display:flex;align-items:center;gap:8px;white-space:nowrap}
.cert-list.left{left:386px}
.cert-list.right{left:611px}

/* testimonials */
.testimonials{top:2344px;height:352px}
.testimonials h2{position:absolute;top:30px;width:100%;text-align:center;font-size:32px;color:var(--blue)}
.quotes{position:absolute;left:234px;top:93px;display:flex;gap:18px}
.quote{width:232px;height:182px;border:1px solid #e1e1e1;border-radius:3px;padding:16px 20px;position:relative}
.quote-top{display:flex;justify-content:space-between;align-items:center;margin-bottom:14px}
.quote-mark{font-size:26px;font-weight:700;color:#333;line-height:14px}
.stars{color:var(--star);font-size:13px;letter-spacing:3px}
.quote p{font-size:9.4px;line-height:15px;color:var(--muted)}
.quote-author{position:absolute;left:20px;top:112px;display:flex;align-items:center;gap:12px}
.avatar{width:48px;height:48px;border-radius:50%;background:#c9c2bb}
.quote-author strong{display:block;font-size:11px;font-weight:500;color:#222;text-transform:uppercase}
.quote-author span{font-size:9.5px;color:var(--blue)}
.dots{position:absolute;left:564px;top:304px;display:flex;gap:4px}
.dots i{width:22px;height:2px;background:#999}
.dots i:first-child{background:var(--blue)}

/* footer */
.site-footer{top:2696px;height:323px;background:var(--dark);color:#aaa}
.subscribe{position:absolute;left:234px;top:31px;display:flex;gap:7px}
.subscribe .field{width:208px;height:32px;background:#3a3a3a;border-radius:2px;font-size:8.5px;color:#777;padding:11px 12px}
.subscribe .btn{width:96px;height:32px;line-height:32px;font-size:9px}
.social{position:absolute;right:234px;top:38px;display:flex;gap:8px}
.social i{width:22px;height:22px;border-radius:50%;background:#3c3c3c;display:block}
.rule{position:absolute;left:234px;top:91px;width:732px;height:1px;background:#3a3a3a}
.foot-brand{position:absolute;left:234px;top:128px;font-size:9px;line-height:20px}
.foot-brand .brand-name{font-size:17px;color:var(--white);display:block;margin-bottom:14px}
.foot-brand b{color:var(--white);font-weight:400}
.foot-col{position:absolute;top:126px;font-size:8.6px;line-height:17.5px}
.foot-col h4{font-size:9.5px;font-weight:700;color:var(--white);text-transform:uppercase;margin-bottom:4px}
.copyright{position:absolute;top:290px;width:100%;text-align:center;font-size:8.5px;color:#888}
.copyright b{color:var(--white);font-weight:500}
</style>
</head>
<body>

<header class="site-header">
  <div class="brand">
    <span class="brand-dot"></span>
    <span class="brand-name">Maren K Holt</span>
  </div>
  <div class="contact-bar">
    <span><svg width="13" height="10" viewBox="0 0 13 10"><rect x=".5" y=".5" width="12" height="9" fill="none" stroke="#1b6496"/><path d="M.5.5l6 5 6-5" fill="none" stroke="#1b6496"/></svg>maren@holtassist.org</span>
    <span><svg width="12" height="12" viewBox="0 0 24 24"><path fill="#1b6496" d="M6.6 10.8a15.1 15.1 0 006.6 6.6l2.2-2.2a1 1 0 011-.24 11.4 11.4 0 003.6.57 1 1 0 011 1V20a1 1 0 01-1 1A17 17 0 013 4a1 1 0 011-1h3.5a1 1 0 011 1c0 1.25.2 2.45.57 3.6a1 1 0 01-.25 1z"/></svg>+66 81 555 0192</span>
  </div>
  <nav class="nav">
    <span class="active">HOME</span><span>SERVICES</span><span>SYSTEM APPLICATIONS</span><span>FEES</span><span>WHY ME?</span><span>CONTACT</span>
  </nav>
</header>

<section class="hero">
  <div class="abs" style="inset:0" role="img" aria-label="Photo of a proofread printed page with red correction marks and a red pen"></div>
  <div class="hero-shade"></div>
  <h1 class="script">Allow me...</h1>
  <p>to handle the details so you can get on with business.</p>
  <a class="btn">Learn More</a>
</section>

<section class="welcome">
  <div class="welcome-band"></div>
  <h2 class="script">Welcome</h2>
  <div class="welcome-text">
    <p>Every great leader is backed by diligent and knowledgeable support. Have you ever wondered what it would be like to have your very own personal assistant? Well, you can. A virtual assistant can do everything a full-time assistant can, with the added bonus that she can save you money. Whether you need daily help, or help with special assignments or big projects, hiring me as your VA will save you the costs typically associated with an employee–holiday pay, sick pay, overtime, taxes, and insurance, are no longer your concern. And, as a virtual assistant, I only charge for the hours I actually work–no more resource-siphoning downtime.</p>
    <p>Allow me to be of service. Answering emails, organizing client files, managing projects, updating website content, proofreading content, they are all important tasks but not so important that you have to do them yourself. I have rescued many businesses from the throws of chaos, bringing order to a seemingly endless onslaught of details and procedures. I can make your business function optimally. And as an independent agent, I can do it for a fraction of the cost of a full-time right-hand assistant.</p>
    <p>From organizing existing businesses to creating systems and procedures to launching a fledgling business, I offer decades of experience mastering the minutiae so your business can function at its optimum.</p>
    <p>So trust your important tasks to a professional specially qualified to handle the mundane and minutiae. Delegate to an expert and restore the life-work balance that will benefit you, your clients, and your personal relationships.</p>
    <p>Isn't it time you hire the right-hand support your business needs and you deserve?</p>
  </div>
  <a class="btn">Learn More</a>
  <div class="portrait" role="img" aria-label="Portrait photo of the virtual assistant"></div>
</section>

<section class="services">
  <h2 class="script">Our Services</h2>
  <p class="services-intro">Do you need some Smart Office Support (SOS)? Do you have a huge project looming on the horizon? Do you just need a little support managing the growing stacks of To-Dos cluttering your desk? As a master of managing the barrage of daily details that require concise and prompt attention, SOS is my speciality, from organisation to proofreading, no detail is too small!</p>
  <div class="cards">
    <div class="card"><div class="card-icon" role="img" aria-label="Project management icon"></div><h3>Organizational/Project<br>Management</h3><p>Reliable project and team management, master of organisation</p><a>Learn More</a></div>
    <div class="card"><div class="card-icon" role="img" aria-label="Accounting icon"></div><h3>Administrative and<br>Accounting Support</h3><p>Work smarter not harder with the right VA by your side</p><a>Learn More</a></div>
    <div class="card"><div class="card-icon" role="img" aria-label="Website icon"></div><h3>Website<br>Administration</h3><p>Dependable and reliable website updates–like clockwork</p><a>Learn More</a></div>
    <div class="card"><div class="card-icon" role="img" aria-label="Editorial icon"></div><h3>Editorial Service<br>/Proofreading</h3><p>Catching simple typos and grammatical faux pas to preserve your integrity</p><a>Learn More</a></div>
  </div>
</section>

<section class="about">
  <h2 class="tagline script">If you want something done right... find the right person to do it!</h2>
  <div class="col col-left">
    <h3 class="script">Why Me?</h3>
    <p>I offer administrative, management, and editorial services for those in need of an expert, professional, and discreet “virtual” assistant. As an independent contractor, I can offer you these services with all the same dedication and loyalty as a full-time staff assistant – at a more cost-effective rate.</p>
    <h3 class="script gap">Who's benefited from my help...</h3>
    <p>My employers and clients hail from backgrounds in marketing, education, import/export businesses, IT, health and wellbeing and hospitality. They range from small to large businesses and individuals, all with a common issue – they needed help managing the day-to-day details that make their operations run smoothly.</p>
    <p>My clients are entrepreneurs, consultants, charitable organisations, small businesses, students and professors – all of whom can attest to the benefits of outsourcing time-consuming tasks that distract them from their primary mission.</p>
    <h3 class="script gap">What I can do for you...</h3>
    <p>Sales accounting, inventory control, social media management, general office support, marketing assistance, client or HR relations, project management, contract reviews, regulatory compliance documentation ... essentially any area of business that can benefit from administrative support, you'll find I can deliver exemplary service. There is no job too big or too small.</p>
    <p>And, as of 2019, I am proud to announce that I am expanding my services to offer editorial services after completing my Professional Certificate for Proofreading. I look forward to offering this service to business and individuals who prepare proposals, investor reports, academic papers, grant writers, and even blog posts and web pages. Let me put the perfect polish on your public prose.</p>
  </div>
  <div class="col col-right">
    <h3 class="script">Sometimes your calling... well, it finds you!</h3>
    <p>I have over 30-years experience rescuing countless businesses from backlogs of work or faulty practices, and I have helped launched almost as many new businesses by building a solid foundation on sound systems. I have a history of arriving in just the right place at just the right time – when businesses and professionals need me the most.</p>
    <p>I have fine-tuned my administration skills and operational and organisational insights over three decades, starting in a local government office in the UK. Over the course of those years, I have amassed experience in accounting, stock purchasing and management, IT support (research, purchase, installation, and maintenance of software), personnel training and management, general PA duties, business compliance (insurance, fire, health &amp; safety regulations), contract management, and human resources services – skills built on a strong foundation of office and administrative expertise.</p>
    <p>After many years in the corporate world as a customer service representative, I landed in the import/export business, coordinating stock production with China (in association with the APAC Operations Director) for distribution throughout the UK, Europe, South Africa, South America, and the USA. Under the Managing Director, I prepared weekly, monthly, and quarterly financial reports for distribution to stakeholders as well as staff. I managed a team effort to plan, coordinate and provide seminars, exhibitions, marketing campaigns, and product launches.</p>
    <p>Before embarking on my own, I was the go-to gal for Talk Well Language, a language school in Thailand, instituting new software systems and procedures to streamline and expedite the management of student records and government compliances documentation (Visas). I managed the school's website development and daily administration, directed email marketing campaigns and liaised with the public, students and businesses, providing a unified image to our community, our target market.</p>
    <p>I am conscientious, meticulous, methodical, diligent and driven. I am a strategic thinker, skilled at organisation and plan execution. I love a challenge and am continually learning new applications and platforms to help me deliver on my promises to you.</p>
    <p>With my help, you never have to wonder if your project will be completed on time or to your standards. I have a very hand-on approach involvement with my clients, their projects and their business.</p>
    <p>Allow me to assist you and restore your work-life balance.</p>
  </div>
</section>

<section class="certs">
  <h2>CERTIFICATIONS AND QUALIFICATIONS</h2>
  <ul class="cert-list left">
    <li><svg width="10" height="8" viewBox="0 0 10 8"><path d="M1 4l3 3 5-6" fill="none" stroke="#fff" stroke-width="1.4"/></svg>Professional Certificate for Proofreading</li>
    <li><svg width="10" height="8" viewBox="0 0 10 8"><path d="M1 4l3 3 5-6" fill="none" stroke="#fff" stroke-width="1.4"/></svg>Diploma for Text and Spreadsheet Software</li>
    <li><svg width="10" height="8" viewBox="0 0 10 8"><path d="M1 4l3 3 5-6" fill="none" stroke="#fff" stroke-width="1.4"/></svg>Thai language – A1</li>
    <li><svg width="10" height="8" viewBox="0 0 10 8"><path d="M1 4l3 3 5-6" fill="none" stroke="#fff" stroke-width="1.4"/></svg>Spanish to GCSE Level – A1</li>
    <li><svg width="10" height="8" viewBox="0 0 10 8"><path d="M1 4l3 3 5-6" fill="none" stroke="#fff" stroke-width="1.4"/></svg>Trade Board Book-keeping Stage 1</li>
  </ul>
  <ul class="cert-list right">
    <li><svg width="10" height="8" viewBox="0 0 10 8"><path d="M1 4l3 3 5-6" fill="none" stroke="#fff" stroke-width="1.4"/></svg>Qualified TEFL teacher</li>
    <li><svg width="10" height="8" viewBox="0 0 10 8"><path d="M1 4l3 3 5-6" fill="none" stroke="#fff" stroke-width="1.4"/></svg>Craft Institute in Public House Management</li>
    <li><svg width="10" height="8" viewBox="0 0 10 8"><path d="M1 4l3 3 5-6" fill="none" stroke="#fff" stroke-width="1.4"/></svg>6 C.S.E. Grade 3 and above, 2 ‘O’ Levels</li>
    <li><svg width="10" height="8" viewBox="0 0 10 8"><path d="M1 4l3 3 5-6" fill="none" stroke="#fff" stroke-width="1.4"/></svg>Many other online courses</li>
  </ul>
</section>

<section class="testimonials">
  <h2 class="script">Testimonials</h2>
  <div class="quotes">
    <div class="quote"><div class="quote-top"><span class="quote-mark">”</span><span class="stars">★★★★★</span></div><p>Lorem ipsum dolor sit amet, consectetur adipiscing elit. Quisque iaculis elementum eleifend. Cras malesuada vitae enim id imperdiet. Vestibulum vestibulum egestas.</p><div class="quote-author"><div class="avatar" role="img" aria-label="Client photo"></div><div><strong>Daniel Moreau</strong><span>Client</span></div></div></div>
    <div class="quote"><div class="quote-top"><span class="quote-mark">”</span><span class="stars">★★★★★</span></div><p>Lorem ipsum dolor sit amet, consectetur adipiscing elit. Quisque iaculis elementum eleifend. Cras malesuada vitae enim id imperdiet. Vestibulum vestibulum egestas.</p><div class="quote-author"><div class="avatar" role="img" aria-label="Client photo"></div><div><strong>Daniel Moreau</strong><span>Client</span></div></div></div>
    <div class="quote"><div class="quote-top"><span class="quote-mark">”</span><span class="stars">★★★★★</span></div><p>Lorem ipsum dolor sit amet, consectetur adipiscing elit. Quisque iaculis elementum eleifend. Cras malesuada vitae enim id imperdiet. Vestibulum vestibulum egestas.</p><div class="quote-author"><div class="avatar" role="img" aria-label="Client photo"></div><div><strong>Daniel Moreau</strong><span>Client</span></div></div></div>
  </div>
  <div class="dots"><i></i><i></i><i></i></div>
</section>

<footer class="site-footer">
  <div class="subscribe"><div class="field">Enter your email...</div><a class="btn">Subscribe</a></div>
  <div class="social" aria-label="Social links"><i></i><i></i><i></i></div>
  <div class="rule"></div>
  <div class="foot-brand">
    <span class="brand-name">Maren K Holt</span>
    Phone: <b>+66 81 555 0192</b><br>
    Email: <b>maren@holtassist.org</b>
  </div>
  <div class="foot-col" style="left:434px"><h4>Services</h4>Organizational/Project Management<br>Administrative and Accounting Support<br>Website Administration<br>Editorial Service/Proofreading</div>
  <div class="foot-col" style="left:654px"><h4>Term of Use</h4>Terms and Conditions<br>Copyright<br>Refund Policy<br>Privacy Policy<br>Disclaimer</div>
  <div class="foot-col" style="left:817px"><h4>More Links</h4>FAQs<br>Contact<br>Blog<br>Work with Us</div>
  <p class="copyright">Copyright © 2020 <b>Maren K Holt</b> All rights reserved.</p>
</footer>

</body>
</html>
```